Website Design for Luxury Product

Are you tired of the "same-old-same-old"?
Would you like to make a difference?
Do you want to make your mark as a designer and work on a full and cool project?
If you answered "YES" to any of the questions above ... keep on reading. We've been looking for you!
Our cigar company www.velmortabacs.com is in need of a new website design.
The look-and-feel needs to ooze luxury, be clean, and exciting.
Our goal is to have people visiting our website walk away and:
1. Understand that we are a high end, luxury cigar company
2. Feel a rapport and excitement with our company
3. Establish credibility
4. Have the visitor want to join our monthly VIP cigar club
Our logo is enclosed below
Frequently Asked Questions:
1. Who Is Your Target Market and What Are Your Demographics?
Our target market is 100% is the US and primarily males between the ages of 33 and 65.
Our target market are successful professionals like investment advisers, bankers, accountants, doctors, and entrepreneurs with a high disposable income.
Our audience has the ability to purchase just about anything they would like but prefer to purchase the highest quality items and don't mind paying a premium for this.
The website must give the visitor confidence that we are the "real thing" and that we are the best-of-the-best.
2. What Will The Website Be Hosted On?
The website will either be hosted as a stand alone website using Control Panel or on a WordPress Site.
3. What Font Should I Use For the Website?
Our standard font is the Gotham Family of Fonts.
4. What Colors Should the Website Use?
Surprise us.
Our goal is to have the website that is modern, hip, cool and oozes luxury.
5. What Look and Feel Should I Use?
Take a look at our newly designed logo which is attached as a file. We are after a look that is modern, clean, and luxurious.
If you think you have the "right stuff" we'd love to hear from you with your design.
Harold and Dwayne
Target Market(s)
Industry/Entity Type
Social Club
Coding
Coded - Design and coding required
Number of Pages Required
5+ page
Font styles to use
Other font styles liked:
- Gotham Family of Fonts
Requirements
Must have
- My project must have a home page and supporting pages with a consistent them that is
- Modern
- Luxurious
- Establishes Credibility
- For the content to use please look to our website with the existing wording.
Nice to have
- Use your imagination on this one.
Should not have
- Our project should not have a look and feel that is ornate and complicated. An example of this is our existing logo which can be found on our website www.velmortabacs.com
- We have moved away from this look.

```html
<!DOCTYPE html>
<html lang="en">
<head>
<meta charset="utf-8">
<title>Velmor Tabacs</title>
<link href="https://fonts.googleapis.com/css2?family=Kotta+One&family=Open+Sans:wght@400;600&family=Yellowtail&display=swap" rel="stylesheet">
<style>
  :root {
    --ink: #1a1a1a;
    --body-grey: #6f6f6f;
    --accent: #d2400f;
    --white: #ffffff;
    --hero-dark: #1c1a19;
    --hero-mid: #4a3a31;
    --band-black: #000000;
    --footer-grey: #2e2e2e;
    --frame: #e4e4e4;
  }
  * { margin: 0; padding: 0; box-sizing: border-box; }
  html, body { width: 718px; height: 1200px; overflow: hidden; }
  body { position: relative; background: var(--white); font-family: "Open Sans", sans-serif; color: var(--ink); }
  .abs { position: absolute; }

  /* Hero */
  .hero { left: 0; top: 0; width: 718px; height: 382px;
    background: radial-gradient(ellipse at 60% 40%, var(--hero-mid) 0%, #2b2421 45%, var(--hero-dark) 100%); }
  .brand-tab { left: 297px; top: 0; width: 124px; height: 82px; }
  .brand-name { left: 297px; top: 22px; width: 124px; text-align: center;
    font-family: "Kotta One", serif; font-size: 15px; letter-spacing: 1px; line-height: 17px; color: var(--ink); }
  .brand-dot { left: 350px; top: 6px; width: 18px; height: 18px; border-radius: 50%; background: var(--ink); }
  .login { left: 88px; top: 52px; display: flex; align-items: center; gap: 5px;
    font-family: "Kotta One", serif; font-size: 8px; color: var(--white); text-transform: uppercase; }
  .search { left: 532px; top: 52px; display: flex; align-items: center; gap: 5px;
    font-family: "Kotta One", serif; font-size: 8px; color: var(--white); text-transform: uppercase; }
  .main-nav { left: 88px; top: 95px; width: 542px; height: 29px; }
  .main-nav svg { position: absolute; left: 0; top: 0; }
  .main-nav ul { position: absolute; left: 0; top: 0; width: 542px; height: 29px; list-style: none;
    display: flex; justify-content: center; align-items: center; gap: 0; }
  .main-nav li { font-family: "Kotta One", serif; font-size: 9.5px; color: var(--white); letter-spacing: .3px; }
  .main-nav li + li::before { content: "\2022"; margin: 0 14px; font-size: 11px; }
  .hero-title { left: 0; top: 150px; width: 718px; text-align: center;
    font-family: "Yellowtail", cursive; font-size: 68px; color: var(--white); }
  .hero-cigar { left: 40px; top: 222px; width: 640px; height: 110px; border-radius: 50px;
    background: radial-gradient(ellipse at center, rgba(150,90,60,.55) 0%, rgba(90,55,35,.3) 50%, rgba(0,0,0,0) 75%); }
  .scroll-down { left: 350px; top: 326px; }

  /* Welcome */
  .welcome-title { left: 0; top: 400px; width: 718px; text-align: center;
    font-family: "Kotta One", serif; font-size: 19px; color: var(--ink); }
  .welcome-text { left: 0; top: 428px; width: 718px; text-align: center;
    font-size: 8.3px; line-height: 12px; color: var(--body-grey); }

  /* VIP */
  .vip-photo-frame { left: 87px; top: 489px; width: 281px; height: 205px; border: 1px solid var(--frame); background: var(--white); }
  .vip-photo { left: 91px; top: 493px; width: 273px; height: 197px;
    background: linear-gradient(135deg, #cfcbc4 0%, #a89f96 45%, #3c3634 75%, #7a4a38 100%); }
  .section-title { font-family: "Kotta One", serif; font-size: 18px; }
  .vip-title { left: 385px; top: 487px; color: var(--ink); }
  .vip-text { left: 385px; top: 523px; width: 240px; font-size: 8.2px; line-height: 12.3px; color: var(--body-grey); }
  .vip-text p + p { margin-top: 12px; }
  .learn-more { font-family: "Kotta One", serif; font-size: 8px; color: var(--accent); text-transform: uppercase;
    display: flex; align-items: center; gap: 5px; letter-spacing: .3px; }
  .vip-more { left: 385px; top: 653px; }

  /* Taste band */
  .taste-band { left: 0; top: 716px; width: 718px; height: 240px; background: var(--band-black); }
  .taste-photo { left: 300px; top: 716px; width: 418px; height: 240px;
    background: radial-gradient(ellipse at 40% 55%, #b06a1e 0%, #5a3310 22%, #2a1a0e 45%, #000 75%); }
  .taste-title { left: 88px; top: 775px; color: var(--white); }
  .taste-text { left: 88px; top: 808px; width: 240px; font-size: 8.2px; line-height: 9.8px; color: var(--white); }
  .taste-text p + p { margin-top: 9px; }
  .taste-more { left: 88px; top: 884px; }

  /* Quote */
  .quote-logo-box { left: 104px; top: 972px; width: 154px; height: 124px; border: 1px solid #d6d6d6; background: var(--white); }
  .quote-logo-dot { left: 164px; top: 990px; width: 34px; height: 34px; border-radius: 50%; background: var(--ink); }
  .quote-logo-name { left: 104px; top: 1036px; width: 154px; text-align: center;
    font-family: "Kotta One", serif; font-size: 20px; line-height: 22px; letter-spacing: 1px; color: var(--ink); }
  .quote-text { left: 289px; top: 995px; width: 330px; font-family: "Kotta One", serif; font-size: 16.5px; line-height: 22px; color: var(--ink); }
  .quote-author { left: 289px; top: 1056px; font-family: "Kotta One", serif; font-size: 10.5px; color: var(--accent); }

  /* Footer */
  .site-footer { left: 0; top: 1114px; width: 718px; height: 86px;
    background: linear-gradient(180deg, #3a3a3a 0%, var(--footer-grey) 50%, #262626 100%); }
  .footer-nav { left: 0; top: 1143px; width: 718px; list-style: none; display: flex; justify-content: center;
    font-family: "Kotta One", serif; font-size: 6px; color: var(--white); }
  .footer-nav li + li::before { content: "|"; margin: 0 10px; }
  .copyright { left: 0; top: 1155px; width: 718px; text-align: center; font-size: 7px; color: var(--white); }
</style>
</head>
<body>

<header>
  <div class="abs hero" role="img" aria-label="Photograph of a man in a flat cap smoking a cigar, with a long cigar and loose tobacco leaf across the frame"></div>
  <div class="abs hero-cigar" role="img" aria-label="Close-up of a long cigar lying horizontally with scattered tobacco"></div>

  <svg class="abs brand-tab" viewBox="0 0 124 82" aria-hidden="true">
    <polygon points="0,0 124,0 124,64 62,82 0,64" fill="#ffffff"/>
  </svg>
  <div class="abs brand-dot"></div>
  <div class="abs brand-name">VELMOR<br>TABACS</div>

  <a class="abs login">
    <svg width="14" height="14" viewBox="0 0 14 14" aria-hidden="true">
      <path d="M6 1h7v12H6" fill="none" stroke="#fff" stroke-width="1.5"/>
      <path d="M1 7h8M6 4l3 3-3 3" fill="none" stroke="#fff" stroke-width="1.5"/>
    </svg>
    Login
  </a>

  <div class="abs search">
    <svg width="13" height="13" viewBox="0 0 13 13" aria-hidden="true">
      <circle cx="5.5" cy="5.5" r="4" fill="none" stroke="#fff" stroke-width="2"/>
      <path d="M8.5 8.5l3.5 3.5" stroke="#fff" stroke-width="2"/>
    </svg>
    Search string here
  </div>

  <nav class="abs main-nav">
    <svg width="542" height="29" viewBox="0 0 542 29" aria-hidden="true">
      <path d="M2 1H528L540 14.5 528 28H2L14 14.5Z M2 1" fill="none" stroke="#fff" stroke-width="1.5"/>
      <path d="M2 1L14 14.5 2 28 M540 1 L528 14.5 540 28" fill="none" stroke="#fff" stroke-width="1.5"/>
    </svg>
    <ul>
      <li>Home</li>
      <li>VIP Club Enrollment</li>
      <li>Our Story</li>
      <li>Taste Profile</li>
      <li>The Velmor Blend</li>
      <li>Contact</li>
    </ul>
  </nav>

  <h1 class="abs hero-title">Truly great cigars</h1>

  <svg class="abs scroll-down" width="18" height="12" viewBox="0 0 18 12" aria-hidden="true">
    <path d="M2 2l7 7 7-7" fill="none" stroke="#fff" stroke-width="3"/>
  </svg>
</header>

<main>
  <section>
    <h2 class="abs welcome-title">Welcome to Velmor Tabacs</h2>
    <p class="abs welcome-text">Our fellow brothers and sisters of the leaf, welcome ... you've arrived.<br>At Velmor Tabacs our mission is to elevate your enjoyment of cigars and life's special moments</p>
  </section>

  <section>
    <div class="abs vip-photo-frame"></div>
    <div class="abs vip-photo" role="img" aria-label="Photograph of a bearded man in a tuxedo smoking a cigar in a leather armchair, holding a glass"></div>
    <h2 class="abs section-title vip-title">VIP Membership</h2>
    <div class="abs vip-text">
      <p>You Are About To Embark On A Journey Unlike Any You Have Ever Experienced.</p>
      <p>Your senses are going to explode with new tastes and textures.</p>
      <p>You will meet accomplished and interesting people, fellow “Brothers (and Sisters) of the Leaf” who share our passion for finding life's “Magic Moments.”</p>
    </div>
    <a class="abs learn-more vip-more">Learn more
      <svg width="6" height="8" viewBox="0 0 6 8" aria-hidden="true"><path d="M1 1l3 3-3 3" fill="none" stroke="#1a1a1a" stroke-width="1.5"/></svg>
    </a>
  </section>

  <section>
    <div class="abs taste-band"></div>
    <div class="abs taste-photo" role="img" aria-label="Photograph of a crystal snifter of amber liquor beside a smoking cigar on a dark wooden surface"></div>
    <h2 class="abs section-title taste-title">A Taste Like None Other</h2>
    <div class="abs taste-text">
      <p>Combine art with science ... seven rare and special tobacco leaves from four countries and you only scratch the surface of the taste profile for the Velmor Cigar.</p>
      <p>Created for the sole purpose of enjoying life's Magic Moments and crafted with our heart and soul.</p>
    </div>
    <a class="abs learn-more taste-more">Learn more
      <svg width="6" height="8" viewBox="0 0 6 8" aria-hidden="true"><path d="M1 1l3 3-3 3" fill="none" stroke="#ffffff" stroke-width="1.5"/></svg>
    </a>
  </section>

  <section>
    <div class="abs quote-logo-box"></div>
    <div class="abs quote-logo-dot"></div>
    <div class="abs quote-logo-name">VELMOR<br>TABACS</div>
    <blockquote class="abs quote-text">"We make a living by what we get, but we make a life by what we give."</blockquote>
    <p class="abs quote-author">-- Edmund Harcourt</p>
  </section>
</main>

<footer>
  <div class="abs site-footer"></div>
  <ul class="abs footer-nav">
    <li>Home</li>
    <li>VIP Club Enrollment</li>
    <li>Our Story</li>
    <li>Taste Profile</li>
    <li>The Velmor Blend</li>
    <li>Contact</li>
  </ul>
  <p class="abs copyright">© 2016 Velmor Tabacs by Grand Oeuvre Estates&nbsp; 418 Alder Lane, Cedar Bay, FL 32114</p>
</footer>

</body>
</html>
```